New VPN Company needs a Web Site

This competition is the first step of a 3 step project.
- Step 1: (This project) We are looking to have 3 pages designed to evaluate your design and illustration skills.
- Step 2: Once we find a winner, we will request a bid to have the rest of the website designed.
- Step 3: We will request a bid to have the designs converted into PressKit if the bid is acceptable.
If you have the capabilities, Steps 2 and 3 can be combined into a single project/bid.
Design Notes
- Design type should be “FLAT.”
- Clean, crisp design that communicates security, anonymity, encryption, privacy.
- Please take a look at the following website: http://brisk.toveltunnel.com This is our current Word Press based setup. It contains all the link structures, menus, and text for the website. PLEASE NOTE THAT THE CURRENT DESIGN HAS NOTHING TO DO WITH WHAT YOU ARE DESIGNING. I USED THE FIRST WORD PRESS TEMPLATE THAT I COULD FIND. Once you submit a winning design, either YOU (if you have the skill set) or somebody else will take the designs and convert it into a word press template.
Here are a few of the pages from http://brisk.toveltunnel.com that I would like to see mockups for:
o Main Page: http://brisk.toveltunnel.com
Notes
• I have a dummy graphic up. That graphic needs to be replaced. Also as per the “Should have’s” I want all pages to have unlimited stretching right and left without that grey border on the right and left sides that are currently present.)
o Features Page: http://brisk.toveltunnel.com/index.php/features/
o Fenestra App download Page: http://brisk.toveltunnel.com/index.php/vpn-apps/vpn-for-windows/

- I want a “top bar” which shows Your IP: Your ISP: Your Location: Your Status: Like most of my competitors have.
- This website needs several original illustrations.
- The website must be clean, uncluttered, and concise.
- Use the copy provided from the http://brisk.toveltunnel.com website.
- Colors are up to the designers; this includes logo colors

- Please take a look at some of our competitor's websites for overall inspiration:
o https://www.quaywardnet.com
o https://bexilvpn.com
o https://www.tovrimesk.com/en-us/index
o https://www.dralmoxvpn.com/
o https://www.glenvixvpn.com/
o https://www.yorbalune.com/
o https://www.plumtavrikvpn.com/en_US/

Target Market(s)

Consumers between 18-30 from around the world.

Industry/Entity Type

Internet Service Provider

Number of Pages Required

3 page

Colors

Designer to choose colors to be used in the design.

Requirements
Must have
• - Look great on Desktop, Tablet, and smartphones.
• - The current template has borders. I want the new design to stretch with the browser, e.g., no grey borders on the left and right of the screen.
• - All illustration work must be original. We are not interested in stock photos.
• - Use attached logo. Font is Nexa Xbold.
Should not have
• - A nonfunctional look on smartphones. A high percentage of purchases will be made by smartphone users.
• - Should only have solid colors (two tone or three tone is ok). I am not a big fan of gradients or soft shadows.

```html
<!DOCTYPE html>
<html lang="en">
<head>
<meta charset="utf-8">
<title>TovelVPN</title>
<link href="https://fonts.googleapis.com/css2?family=Montserrat:wght@400;500;600;700&family=Open+Sans:wght@400;600&display=swap" rel="stylesheet">
<style>
:root{
  --accent:#ef5540;
  --ink:#2b2b2b;
  --muted:#6e6e6e;
  --band:#dcdcdc;
  --card:#eeeeee;
  --line:#e2e2e2;
  --white:#ffffff;
  --footer:#efefef;
}
*{box-sizing:border-box;margin:0;padding:0}
html,body{width:1200px;height:3845px;overflow:hidden}
body{font-family:"Open Sans",Arial,sans-serif;color:var(--ink);background:var(--white);position:relative}
section,header,footer{position:relative;width:1200px}
.abs{position:absolute}
.head-font{font-family:"Montserrat",Arial,sans-serif}

/* header */
.site-header{height:100px;background:var(--white)}
.brand{left:218px;top:18px;display:flex;flex-direction:column;align-items:center;gap:4px}
.brand-dot{width:34px;height:34px;border-radius:50%;background:var(--accent)}
.brand-name{font-family:"Montserrat",sans-serif;font-weight:700;font-size:12px;color:var(--accent)}
.main-nav{left:540px;top:38px;display:flex;gap:14px;font-family:"Montserrat",sans-serif;font-size:12.5px;font-weight:500;color:#333;text-transform:uppercase}
.nav-sep{left:935px;top:32px;width:1px;height:28px;background:#ccc}
.search{left:965px;top:37px}
.badge{left:905px;top:78px;width:50px;height:50px;border-radius:50%;background:var(--accent);border:4px solid var(--white);z-index:2}

/* hero */
.hero{height:505px;background:var(--band)}
.hero h1{left:218px;top:100px;font-family:"Montserrat",sans-serif;font-weight:600;font-size:76px;color:#2f2f2f;letter-spacing:1px}
.hero-lead{left:220px;top:195px;width:360px;font-size:16px;line-height:29px;color:var(--muted)}
.btn{background:var(--accent);color:var(--white);font-family:"Montserrat",sans-serif;display:flex;align-items:center;justify-content:center}
.hero .btn{left:220px;top:317px;width:170px;height:48px;font-size:15px}
.hero-note{left:220px;top:375px;font-size:9.5px;color:#333}
.hero-art{left:615px;top:90px;width:330px;height:310px;border-radius:8px;background:linear-gradient(160deg,#eaeaea,#c9c9c9)}
.slide-arrow{top:228px;width:50px;height:78px;background:var(--accent);display:flex;align-items:center;justify-content:center}
.slide-arrow.prev{left:0}
.slide-arrow.next{left:1150px}

/* features */
.features{height:615px;background:var(--white)}
.feature{width:340px;display:flex;gap:10px}
.feature-num{font-family:"Montserrat",sans-serif;font-size:44px;line-height:40px;color:#bdbdbd;font-weight:400}
.feature h3{font-family:"Montserrat",sans-serif;font-size:19px;line-height:29px;font-weight:600;color:#222;margin-bottom:8px}
.feature p{font-size:10.5px;line-height:21px;color:#444}

/* solution */
.solution{height:435px;background:var(--band)}
.solution h2{left:220px;top:128px;width:370px;font-family:"Montserrat",sans-serif;font-weight:400;font-size:21px;line-height:29px;color:#333}
.solution h2 strong{color:var(--accent);font-weight:700;font-size:28px}
.solution p{left:220px;top:200px;width:370px;font-size:10.5px;line-height:22px;color:#777}
.solution .btn{left:220px;top:282px;width:124px;height:34px;font-size:11px}
.solution-art{left:645px;top:60px;width:330px;height:335px;border-radius:50%;background:radial-gradient(circle,#f4f4f4 0%,#cfd8c6 55%,var(--band) 72%)}

/* pricing */
.pricing{height:560px;background:var(--white)}
.pricing h2{left:0;top:60px;width:1200px;text-align:center;font-family:"Montserrat",sans-serif;font-weight:400;font-size:27px;color:#333}
.pricing h2 strong{color:var(--accent);font-weight:700;font-size:36px}
.pricing .sub{left:0;top:105px;width:1200px;text-align:center;font-family:"Montserrat",sans-serif;font-weight:600;font-size:19px;color:#333}
.plan{top:165px;width:240px;height:325px;background:var(--card);box-shadow:0 2px 6px rgba(0,0,0,.15);text-align:center}
.plan h3{margin-top:45px;font-family:"Montserrat",sans-serif;font-weight:700;font-size:17px;color:#222}
.price{margin-top:38px;color:var(--accent);font-family:"Montserrat",sans-serif;font-size:17px}
.price b{font-size:36px;font-weight:600}
.save{margin-top:34px;font-size:12.5px;color:#333}
.guarantee{margin-top:28px;font-size:13px;color:#333}
.plan .btn{margin:18px auto 0;width:100px;height:26px;font-size:9.5px}

/* why */
.why{height:415px;background:var(--band)}
.why-art{left:220px;top:65px;width:380px;height:290px;border-radius:10px;background:linear-gradient(160deg,#cfe6f5,#8cc5ea)}
.why .kicker{left:620px;top:80px;font-size:16px;color:#666}
.why h2{left:620px;top:100px;font-family:"Montserrat",sans-serif;font-weight:400;font-size:21px;color:var(--accent)}
.why .lead{left:620px;top:140px;width:300px;font-size:16.5px;line-height:21px;color:#444}
.why ul{left:620px;top:225px;list-style:none;font-size:9.5px;color:#666}
.why li{height:31px;padding-left:18px;position:relative}
.why li::before{content:"";position:absolute;left:0;top:6px;width:4px;height:4px;border-radius:50%;background:#999}

/* benefit table */
.benefits{height:890px;background:var(--white)}
.benefit-table{left:220px;top:30px;width:760px;border-collapse:collapse;font-size:12px;color:#333}
.benefit-table th{height:40px;background:#eeeeee;color:var(--accent);font-family:"Montserrat",sans-serif;font-weight:500;font-size:14px;text-align:left;padding-left:16px}
.benefit-table th.check,.benefit-table td.check{width:55px;text-align:center;padding:0;border-left:1px solid var(--line)}
.benefit-table td{height:63px;border-top:1px solid var(--line);padding-left:16px}
.benefit-table tr{border-left:1px solid var(--line);border-right:1px solid var(--line)}
.benefit-table tbody tr:last-child td{border-bottom:1px solid var(--line)}

/* footer */
.site-footer{height:325px;background:var(--footer)}
.site-footer .brand{left:580px;top:45px}
.foot-links{left:0;top:147px;width:1200px;text-align:center;font-family:"Montserrat",sans-serif;font-size:12.5px;line-height:22px;color:#333}
.foot-links span{margin:0 8px;color:#555}
.foot-rule{left:220px;top:215px;width:760px;height:1px;background:#d8d8d8}
.credit{left:0;top:250px;width:1200px;text-align:center;font-size:11px;color:#444;word-spacing:2px}
</style>
</head>
<body>

<header class="site-header">
  <div class="abs brand"><span class="brand-dot"></span><span class="brand-name">TovelVPN</span></div>
  <nav class="abs main-nav"><span>Home</span><span>Features</span><span>VPN Apps</span><span>Pricing</span><span>Support Center</span></nav>
  <span class="abs nav-sep"></span>
  <svg class="abs search" width="12" height="12" viewBox="0 0 12 12"><circle cx="5" cy="5" r="3.6" fill="none" stroke="#333" stroke-width="1.6"/><line x1="7.7" y1="7.7" x2="11" y2="11" stroke="#333" stroke-width="1.8"/></svg>
  <span class="abs badge"></span>
</header>

<section class="hero">
  <h1 class="abs">TovelVPN</h1>
  <p class="abs hero-lead">is a fast and ultra secure offshore based VPN solution with thousands of servers in over 40 countries around the globe</p>
  <a class="abs btn">Get Started Now</a>
  <p class="abs hero-note">OpenTunnel, IKEv2, L2TP/IPSec Tunnels for only $x / mo*</p>
  <div class="abs hero-art" role="img" aria-label="Illustration of a cloud connected to devices, mail, media and files with a hand tapping"></div>
  <div class="abs slide-arrow prev"><svg width="12" height="18" viewBox="0 0 12 18"><polyline points="9,2 3,9 9,16" fill="none" stroke="#fff" stroke-width="2"/></svg></div>
  <div class="abs slide-arrow next"><svg width="12" height="18" viewBox="0 0 12 18"><polyline points="3,2 9,9 3,16" fill="none" stroke="#fff" stroke-width="2"/></svg></div>
</section>

<section class="features">
  <div class="abs feature" style="left:218px;top:60px"><span class="feature-num">1</span><div><h3>Military grade 256 bit encryption</h3><p>Nobody can spy on your internet activities because we route it through securely encrypted tunnels. TovelVPN uses strong AES 256 encryption to ensure that your data is totally secure.</p></div></div>
  <div class="abs feature" style="left:618px;top:60px"><span class="feature-num">2</span><div><h3>Absolute NO LOGGING Policy</h3><p>We do not permanently log any of your online activities. This ensures total privacy and anonymity.</p></div></div>
  <div class="abs feature" style="left:218px;top:220px"><span class="feature-num">3</span><div><h3>Watch Your Favorite Streaming Channels</h3><p>TovelVPN works flawlessly with your favorite streaming channels such as Flixora, Lumo etc. Your ISP might monitor your activity and throttle your internet speed. When using TovelVPN your ISP only sees encrypted data and is unable to throttle your internet speed based on your activity. TovelVPN allows you to bypass location-based blocks and access global streaming services no matter your physical location.</p></div></div>
  <div class="abs feature" style="left:618px;top:220px"><span class="feature-num">4</span><div><h3>P2P Friendly</h3><p>Nobody can spy on your internet activities because we route it through securely encrypted tunnels. TovelVPN uses strong AES 256 encryption to ensure that your data is totally secure.</p></div></div>
  <div class="abs feature" style="left:218px;top:445px"><span class="feature-num">5</span><div><h3>Multiple Devices</h3><p>Use TovelVPN on 10 devices simultaneously</p></div></div>
  <div class="abs feature" style="left:618px;top:445px"><span class="feature-num">6</span><div><h3>Secure your public Wi-Fi connections</h3><p>Use any public Wi-Fi network knowing that nobody can intercept your traffic or spy on you.</p></div></div>
</section>

<section class="solution">
  <h2 class="abs"><strong>TovelVPN</strong> is complete solution for you Business</h2>
  <p class="abs">Lorem ipsum dolor sit amet, consectetur adipiscing elit. Aenean sem dolortus, quis nec erat quam dignissimus. Nimmo deserunt odio molestiae voluptatem ut enim ad minim quis? Fusce consequat, excepteur sit in mi.</p>
  <a class="abs btn">Read More</a>
  <div class="abs solution-art" role="img" aria-label="Illustration of a green open box with colourful web platform badges bursting out"></div>
</section>

<section class="pricing">
  <h2 class="abs"><strong>31 Day</strong> Unconditional</h2>
  <p class="abs sub">Money Back Guarantee</p>
  <div class="abs plan" style="left:220px"><h3>MONTHLY</h3><p class="price">$<b>10.95</b>/month</p><p class="save">NO SAVINGS</p><p class="guarantee">31 Day Money Back Guarantee</p><a class="btn">Get TovelVPN</a></div>
  <div class="abs plan" style="left:480px"><h3>MONTHLY</h3><p class="price">$<b>3.51</b>/month</p><p class="save">SAVE 68%</p><p class="guarantee">31 Day Money Back Guarantee</p><a class="btn">Get TovelVPN Now</a></div>
  <div class="abs plan" style="left:740px"><h3>MONTHLY</h3><p class="price">$<b>10.95</b>/month</p><p class="save">SAVE 52%</p><p class="guarantee">31 Day Money Back Guarantee</p><a class="btn">Get TovelVPN</a></div>
</section>

<section class="why">
  <div class="abs why-art" role="img" aria-label="Illustration of a server in a cloud sending blue arrows to a computer, phone, laptop and other devices"></div>
  <p class="abs kicker">Why Choose Us</p>
  <h2 class="abs">WHY CLIENTS PREFER OUR SERVICES</h2>
  <p class="abs lead">We are on a mission to build, grow and maintain loyal communities at every touchpoint</p>
  <ul class="abs">
    <li>Nulla consequat massa quis enim</li>
    <li>Donec pede justo, fringilla vel, aliquet nec</li>
    <li>arcu. In enim justo, rhoncus ut, imperdiet a, venenatis</li>
    <li>arcu. In enim justo, rhoncus ut, imperdiet a, venenatis</li>
  </ul>
</section>

<section class="benefits">
  <table class="abs benefit-table">
    <thead><tr><th>Benefit</th><th class="check">Check</th></tr></thead>
    <tbody>
      <tr><td>Benefit&nbsp; Check</td><td class="check"><svg width="11" height="9" viewBox="0 0 11 9"><polyline points="1,4.5 4,7.5 10,1" fill="none" stroke="#ef5540" stroke-width="1.8"/></svg></td></tr>
      <tr><td>Apps for all of your favorite devices</td><td class="check"><svg width="11" height="9" viewBox="0 0 11 9"><polyline points="1,4.5 4,7.5 10,1" fill="none" stroke="#ef5540" stroke-width="1.8"/></svg></td></tr>
      <tr><td>X000 IP addresses from across the globe</td><td class="check"><svg width="11" height="9" viewBox="0 0 11 9"><polyline points="1,4.5 4,7.5 10,1" fill="none" stroke="#ef5540" stroke-width="1.8"/></svg></td></tr>
      <tr><td>256 bit AES encryption</td><td class="check"><svg width="11" height="9" viewBox="0 0 11 9"><polyline points="1,4.5 4,7.5 10,1" fill="none" stroke="#ef5540" stroke-width="1.8"/></svg></td></tr>
      <tr><td>OpenTunnel/IKEv2/L2TP/IPsec/PPTP/SSTP protocol support</td><td class="check"><svg width="11" height="9" viewBox="0 0 11 9"><polyline points="1,4.5 4,7.5 10,1" fill="none" stroke="#ef5540" stroke-width="1.8"/></svg></td></tr>
      <tr><td>Strict NO-LOGGING policy</td><td class="check"><svg width="11" height="9" viewBox="0 0 11 9"><polyline points="1,4.5 4,7.5 10,1" fill="none" stroke="#ef5540" stroke-width="1.8"/></svg></td></tr>
      <tr><td>P2P Friendly / Unlimited P2P traffic</td><td class="check"><svg width="11" height="9" viewBox="0 0 11 9"><polyline points="1,4.5 4,7.5 10,1" fill="none" stroke="#ef5540" stroke-width="1.8"/></svg></td></tr>
      <tr><td>Unblock Streaming Services and watch Flixora/Lumo/Vistabox and more</td><td class="check"><svg width="11" height="9" viewBox="0 0 11 9"><polyline points="1,4.5 4,7.5 10,1" fill="none" stroke="#ef5540" stroke-width="1.8"/></svg></td></tr>
      <tr><td>31 Day UNCONDITIONAL money back guarantee</td><td class="check"><svg width="11" height="9" viewBox="0 0 11 9"><polyline points="1,4.5 4,7.5 10,1" fill="none" stroke="#ef5540" stroke-width="1.8"/></svg></td></tr>
      <tr><td>Use on up to X devices simultaneously</td><td class="check"><svg width="11" height="9" viewBox="0 0 11 9"><polyline points="1,4.5 4,7.5 10,1" fill="none" stroke="#ef5540" stroke-width="1.8"/></svg></td></tr>
      <tr><td>Anonymous torrenting</td><td class="check"><svg width="11" height="9" viewBox="0 0 11 9"><polyline points="1,4.5 4,7.5 10,1" fill="none" stroke="#ef5540" stroke-width="1.8"/></svg></td></tr>
      <tr><td>SOCKS5 Web Proxy</td><td class="check"><svg width="11" height="9" viewBox="0 0 11 9"><polyline points="1,4.5 4,7.5 10,1" fill="none" stroke="#ef5540" stroke-width="1.8"/></svg></td></tr>
    </tbody>
  </table>
</section>

<footer class="site-footer">
  <div class="abs brand"><span class="brand-dot"></span><span class="brand-name">TovelVPN</span></div>
  <p class="abs foot-links">VPN FOR FENESTRA<span>|</span>VPN FOR ORCHARD OS<span>|</span>VPN FOR ORCHARD PHONE AND TABLET<br>VPN FOR DROIDEL<span>|</span>VPN FOR CHROMIS</p>
  <span class="abs foot-rule"></span>
  <p class="abs credit">glimmer &nbsp;&nbsp;&nbsp;&nbsp; Theme by Hueforge Powered by PressKit</p>
</footer>

</body>
</html>
```